Letter Head Design

I need a letter head design based on my company logo that I attached.
Include phone number: (403)582-3140
Address: 417 Brindlewood Avenue NE, Calgary, Alberta, Canada, T3M 4K8

Industry/Entity Type

It Company

```html
<!DOCTYPE html>
<html lang="en">
<head>
<meta charset="utf-8">
<title>Lumera Interiors Corp. — Letterhead</title>
<link href="https://fonts.googleapis.com/css2?family=Questrial&display=swap" rel="stylesheet">
<style>
  :root {
    --backdrop: #e6e7e9;
    --paper: #ffffff;
    --brand-blue: #1a6dbf;
    --brand-green: #5bb82a;
    --rule-grey: #d6d9dc;
    --text-white: #ffffff;
  }
  * { margin: 0; padding: 0; box-sizing: border-box; }
  html, body {
    width: 1200px;
    height: 762px;
    overflow: hidden;
    background: var(--backdrop);
    font-family: "Questrial", "Century Gothic", sans-serif;
  }
  .letterhead {
    position: absolute;
    left: 330px;
    top: 28px;
    width: 540px;
    height: 706px;
    background: var(--paper);
    box-shadow: 0 2px 10px rgba(0,0,0,0.12);
  }
  .letterhead__brand {
    position: absolute;
    left: 38px;
    top: 40px;
    display: flex;
    align-items: center;
    gap: 10px;
  }
  .brand-mark {
    width: 34px;
    height: 34px;
    background: var(--brand-green);
    border-radius: 3px;
  }
  .brand-name {
    font-size: 25px;
    color: var(--brand-blue);
    letter-spacing: 0.2px;
  }
  .letterhead__phone {
    position: absolute;
    right: 38px;
    top: 44px;
    display: flex;
    align-items: center;
    gap: 8px;
    font-size: 15px;
    color: var(--brand-blue);
  }
  .phone-icon { width: 20px; height: 16px; }
  .letterhead__rule {
    position: absolute;
    left: 300px;
    right: 38px;
    top: 72px;
    height: 1px;
    background: var(--rule-grey);
  }
  .letterhead__footer {
    position: absolute;
    left: 0;
    right: 0;
    bottom: 40px;
    height: 40px;
  }
  .footer-accent {
    position: absolute;
    left: 80px;
    right: 0;
    top: 6px;
    height: 2px;
    background: var(--brand-green);
  }
  .footer-band {
    position: absolute;
    left: 80px;
    right: 0;
    top: 12px;
    height: 24px;
    background: var(--brand-blue);
    display: flex;
    align-items: center;
    justify-content: center;
    color: var(--text-white);
    font-size: 12px;
    letter-spacing: 1px;
  }
  .footer-mark {
    position: absolute;
    left: 38px;
    top: 2px;
    width: 36px;
    height: 36px;
    background: var(--paper);
    display: flex;
    align-items: center;
    justify-content: center;
  }
  .footer-mark span {
    width: 28px;
    height: 28px;
    background: var(--brand-green);
    border-radius: 3px;
  }
</style>
</head>
<body>
  <article class="letterhead">
    <header class="letterhead__brand">
      <div class="brand-mark"></div>
      <div class="brand-name">Lumera Interiors Corp.</div>
    </header>
    <div class="letterhead__phone">
      <span class="phone-number">(403)582-3140</span>
      <svg class="phone-icon" viewBox="0 0 20 16" aria-hidden="true">
        <path d="M1 6 Q10 -1 19 6 L16 8 L13 6 L13 4 Q10 3 7 4 L7 6 L4 8 Z" fill="#5bb82a"/>
        <path d="M5 9 L15 9 L17 15 L3 15 Z" fill="#5bb82a"/>
        <circle cx="10" cy="12" r="1.8" fill="#ffffff"/>
      </svg>
    </div>
    <div class="letterhead__rule"></div>

    <footer class="letterhead__footer">
      <div class="footer-accent"></div>
      <div class="footer-band">417 Brindlewood Avenue NE, Calgary, Alberta, Canada, T3M 4K8</div>
      <div class="footer-mark"><span></span></div>
    </footer>
  </article>
</body>
</html>
```